New website design for 7vlink

REQUEST FOR PROPOSAL FOR THE DEVELOPMENT 7VLINK WEBSITE

About 7VLINK

7VLINK Nigeria Ltd (7VLINK) is privately owned provider of Information and Communication Technology solutions. The Company has been engaged in Fibre Optic deployments, Wireless Deployments, IP/Data Communication Deployment, Enterprise Network & Infrastructure Solutions and Business Critical infrastructure Management to clients in both private and public sectors. . For more information, please visit www.7vlinkgroup.example .

Project Background.

7VLINK is currently about to roll out her Internet services to both Corporate and Residential market type customers. We need to develop a new site with appeal to the Nigerian market (we must have black people in pictures if we decide to use people but it can also be mixed) but yet have an international appeal. The business has been split into 3 critical service areas:
1. ISP Services
2. Technology Projects
3. Managed Services

The fourth one which more of an activity is 4. Innovation Center

Full Project Scope

Look and feel

We need a website that is CMS (Content Management System) based and that would have WOW! effect on visitor (simple, clean, yet futuristic and techy) , also it is important to try to capture visitors to the website by providing an online chat function. Please visit: http://layoutbazaar.example/item/brightops-premium-responsive-wordpress-theme/full_screen_preview/5816402 (this is almost exactly what we want and can serve as guide for design). You can also visit http://www.7vlinkgroup.example/demowp/ (see a sample of what someone did but we were not too impressed. the site is not neat/crisp. The theme pictures are content should be useful as well).

We have also come across some other inspiration web themes/layout that you may find useful for reference:
1. http://velmorstudio.example/wp-content/uploads/2012/03/kpx7.jpg
2. http://www.artpooler.example/design/6409281
3. http://taskmeadow.example/index

Please use our 7VLINK logo to guide your color theme for our website

Top Navigation

Again using http://layoutbazaar.example/item/brightops-premium-responsive-wordpress-theme/full_screen_preview/5816402 ( i.e where home , About, gallery, portolio, news, Contacts) as reference we would want the following 3 main navigation buttons only ( Which you will notice is in harmony with our logo “ Bridges , Answers, Horizons):
The Top three Navigation Buttons

1. People (Main Menu)
a. About Us
b. Team
c. Customers
d. Partners
e. Investor Relation
f. Contact Us
2. Solutions ( Main Menu)
a. Internet Services (sub menu)
i. Residential Users
ii. Business

b. Technology Projects (sub menu)
i. Plorvex Advanced Services
ii. Networks and Infrastructure
iii. Software & Enterprise Apps
iv. Systems Integration

c. Managed Services (sub menu)
i. Managed IT
ii. Sky Harbor
iii. Data Center & Co-location
iv. Managed PBX
v. Managed Video Conferencing

3. Possibilities ( Main Menu)
a. 7VLINK Labs
b. Co-innovation
c. Angel investments

The main pictures and Slides
Again using http://layoutbazaar.example/item/brightops-premium-responsive-wordpress-theme/full_screen_preview/5816402 as reference the slide Please refer and replace:
1. “Everything starts with a GREAT SOLUTIONS” please replace with “Access Reliable and High Speed INTERNET SERVICES”
2. “ Innovative ways PERFECT RESULTS” Please replace with “ Reduce IT costs, Focus on your Business - MANAGED SERVICES
3. “A driving force IN YOUR BUSINESS” please replace with “ Leverage on our Pool of Certified specialist for your TECHNOLOGY PROJECTS”
4. “The one and only the best IT COMPANY” please replace with “ We Pioneer and seek to Solve Challenges at our INNOVATION CENTER
Please look for appropriate theme pictures to represent the slides above and also reference http://www.7vlinkgroup.example/demowp/

Industry/Entity Type

Communication

Requirements
Nice to have
• Must haves: content management system in the long run so we can put updates.SEO and very light and fast loading of the webpages.

```html
<!DOCTYPE html>
<html lang="en">
<head>
<meta charset="utf-8">
<title>7VLINK — Bridges, Answers, Horizons</title>
<link rel="stylesheet" href="https://fonts.googleapis.com/css2?family=Arimo:wght@400;700&family=Roboto+Condensed:wght@400;700&display=swap">
<style>
  :root {
    --topbar: #3a3a3a;
    --header-bg: #e9e9e9;
    --nav-top: #55629a;
    --nav-bottom: #2e3a6c;
    --nav-line: #6b77ab;
    --navy: #3b4678;
    --panel: #4a5282;
    --accent-green: #8cc63f;
    --link-blue: #3a63a8;
    --ink: #3a3a3a;
    --muted: #7a7a7a;
    --section-bg: #f6f6f6;
    --band-blue: #3f6fa0;
    --footer-bg: #353535;
    --footer-bottom: #2a2a2a;
    --footer-text: #a5a5a5;
  }
  * { box-sizing: border-box; margin: 0; padding: 0; }
  html, body { width: 936px; height: 1200px; overflow: hidden; }
  body { position: relative; background: var(--header-bg); font-family: "Arimo", Arial, sans-serif; color: var(--ink); }

  .topbar { position: absolute; left: 0; top: 0; width: 936px; height: 27px; background: var(--topbar); }
  .topbar__mail { position: absolute; right: 16px; top: 7px; font-size: 11px; color: #9a9a9a; display: flex; align-items: center; gap: 5px; }

  .brand { position: absolute; left: 12px; top: 56px; display: flex; align-items: center; gap: 8px; }
  .brand__dot { width: 34px; height: 34px; border-radius: 50%; background: var(--accent-green); }
  .brand__text { display: flex; flex-direction: column; }
  .brand__name { font-family: "Arimo", Arial, sans-serif; font-weight: 700; font-size: 28px; color: var(--navy); line-height: 1; }
  .brand__tag { font-size: 8px; color: var(--muted); margin-top: 3px; }

  .search { position: absolute; left: 693px; top: 68px; width: 235px; height: 28px; display: flex; border: 1px solid #cfcfcf; background: #fff; }
  .search__field { flex: 1; font-size: 10px; color: #666; padding: 8px 8px; }
  .search__btn { width: 27px; border-left: 1px solid #cfcfcf; background: #f3f3f3; display: flex; align-items: center; justify-content: center; }

  .mainnav { position: absolute; left: 8px; top: 131px; width: 920px; height: 52px; border-radius: 5px 5px 0 0; background: linear-gradient(var(--nav-top), var(--nav-bottom)); display: flex; }
  .mainnav__item { color: #fff; font-weight: 700; font-size: 14.5px; line-height: 52px; text-align: center; white-space: nowrap; border-right: 1px solid var(--nav-line); flex: none; }
  .mainnav__item:last-child { border-right: none; }

  .hero { position: absolute; left: 8px; top: 183px; width: 920px; height: 320px; background: linear-gradient(100deg, #f2f2f2 0%, #ffffff 55%, #e8e8e8 100%); border-bottom: 5px solid var(--navy); }
  .hero__title { position: absolute; left: 89px; top: 110px; font-family: "Roboto Condensed", Arial, sans-serif; font-weight: 700; color: #3a3a3a; }
  .hero__title-lead { display: block; font-size: 30px; letter-spacing: 0.3px; }
  .hero__title-sub { display: block; font-size: 23px; margin-top: 6px; }
  .hero__art { position: absolute; left: 501px; top: 24px; width: 344px; height: 269px; }
  .hero__arrow { position: absolute; top: 149px; width: 22px; height: 22px; border-radius: 50%; background: var(--accent-green); }
  .hero__arrow--prev { left: 20px; }
  .hero__arrow--next { left: 878px; }

  .services { position: absolute; left: 8px; top: 508px; width: 920px; height: 325px; background: var(--section-bg); }
  .services__heading { position: absolute; left: 32px; top: 33px; width: 611px; height: 26px; background: #e8e8e8; }
  .services__heading span { position: absolute; left: 35px; top: -2px; padding: 0 12px; background: var(--section-bg); font-family: "Roboto Condensed", Arial, sans-serif; font-weight: 700; font-size: 22px; color: #2f2f2f; line-height: 30px; }
  .service { position: absolute; top: 88px; width: 196px; }
  .service__photo { width: 196px; height: 96px; }
  .service__caption { height: 35px; background: #ececec; border-bottom: 1px solid #dcdcdc; font-size: 11px; line-height: 35px; padding-left: 8px; color: #444; text-transform: uppercase; white-space: nowrap; overflow: hidden; }
  .service__caption em { font-style: normal; color: var(--link-blue); }
  .service__text { margin-top: 6px; font-size: 9.5px; line-height: 15px; color: var(--muted); letter-spacing: 0.2px; }
  .mission { position: absolute; left: 673px; top: 33px; width: 216px; height: 251px; background: var(--panel); padding: 14px 14px; color: #fff; font-size: 10.5px; line-height: 19.5px; }
  .mission strong { font-weight: 400; color: var(--accent-green); font-size: 12px; }

  .partners { position: absolute; left: 0; top: 833px; width: 936px; height: 83px; background: #fff; display: flex; align-items: center; justify-content: center; gap: 22px; }
  .partners__badge { height: 22px; border-radius: 4px; background: #c9c9c9; }
  .partners__rule { width: 1px; height: 24px; background: #c4c4c4; }

  .band { position: absolute; left: 0; top: 916px; width: 936px; height: 12px; background: var(--band-blue); }

  .footer { position: absolute; left: 0; top: 928px; width: 936px; height: 241px; background: var(--footer-bg); }
  .footer__col { position: absolute; top: 44px; }
  .footer__title { font-size: 11.5px; font-weight: 700; color: #fff; letter-spacing: 0.3px; margin-bottom: 11px; }
  .footer__link { display: block; font-size: 10px; color: var(--footer-text); line-height: 16.5px; }
  .footer__social { position: absolute; left: 749px; top: 43px; display: flex; gap: 12px; }
  .footer__social span { width: 27px; height: 27px; border-radius: 50%; background: #5a5a5a; }
  .footer__brand { position: absolute; left: 744px; top: 89px; width: 153px; height: 59px; background: #fff; display: flex; align-items: center; justify-content: center; gap: 6px; }
  .footer__brand .brand__dot { width: 24px; height: 24px; }
  .footer__brand .brand__name { font-size: 20px; }

  .copyright { position: absolute; left: 0; top: 1169px; width: 936px; height: 31px; background: var(--footer-bottom); font-size: 10px; color: #6c6c6c; line-height: 31px; padding-left: 53px; }
</style>
</head>
<body>
  <div class="topbar">
    <div class="topbar__mail">
      <svg width="11" height="8" viewBox="0 0 11 8"><rect x="0.5" y="0.5" width="10" height="7" fill="none" stroke="#9a9a9a"/><path d="M0.5 0.5 L5.5 4.5 L10.5 0.5" fill="none" stroke="#9a9a9a"/></svg>
      info@7vlinkgroup.example
    </div>
  </div>

  <div class="brand">
    <span class="brand__dot"></span>
    <div class="brand__text">
      <span class="brand__name">7vlink</span>
      <span class="brand__tag">Bridges • Answers • Horizons</span>
    </div>
  </div>

  <div class="search">
    <div class="search__field">Enter your search here...</div>
    <div class="search__btn">
      <svg width="10" height="10" viewBox="0 0 10 10"><circle cx="4" cy="4" r="3" fill="none" stroke="#444" stroke-width="1.5"/><path d="M6.3 6.3 L9 9" stroke="#444" stroke-width="1.6"/></svg>
    </div>
  </div>

  <nav class="mainnav">
    <span class="mainnav__item" style="width:85px">Home</span>
    <span class="mainnav__item" style="width:87px">People</span>
    <span class="mainnav__item" style="width:111px">About Us</span>
    <span class="mainnav__item" style="width:76px">Team</span>
    <span class="mainnav__item" style="width:121px">Customers</span>
    <span class="mainnav__item" style="width:103px">Partners</span>
    <span class="mainnav__item" style="width:153px">Investor Relation</span>
    <span class="mainnav__item" style="width:184px">Contact Us</span>
  </nav>

  <section class="hero">
    <span class="hero__arrow hero__arrow--prev"></span>
    <h1 class="hero__title">
      <span class="hero__title-lead">ACCESS RELIABLE AND</span>
      <span class="hero__title-sub">HIGH SPEED INTERNET SERVICES</span>
    </h1>
    <svg class="hero__art" role="img" aria-label="Illustration of a glowing blue globe set among white and blue square tiles" viewBox="0 0 344 269">
      <defs>
        <linearGradient id="tileGrad" x1="0" y1="0" x2="1" y2="1">
          <stop offset="0" stop-color="#ffffff"/>
          <stop offset="0.5" stop-color="#b9d3e8"/>
          <stop offset="1" stop-color="#5f8fbd"/>
        </linearGradient>
      </defs>
      <rect x="0" y="0" width="344" height="269" fill="url(#tileGrad)" opacity="0.55"/>
    </svg>
    <span class="hero__arrow hero__arrow--next"></span>
  </section>

  <section class="services">
    <div class="services__heading"><span>SERVICES</span></div>

    <article class="service" style="left:32px">
      <div class="service__photo" role="img" aria-label="Photo of a finger pressing a keyboard key" style="background:linear-gradient(135deg,#1c2f6b,#6f87c4 60%,#dfe4ef)"></div>
      <div class="service__caption"><em>Plorvex</em> Advanced Services</div>
      <p class="service__text">We provide a consultative approach in our Plorvex service offerings through advanced services in security and unified comm­unications and other high-end network...</p>
    </article>

    <article class="service" style="left:240px">
      <div class="service__photo" role="img" aria-label="Photo of a professional sketching technology and cloud diagrams" style="background:linear-gradient(135deg,#0f3f55,#2f7d95 55%,#c7dbe2)"></div>
      <div class="service__caption">Technology <em>Training</em></div>
      <p class="service__text">In today's world, IT professionals need to stay ahead of the pack by constantly acquiring newskills and developing competencies through training...</p>
    </article>

    <article class="service" style="left:447px">
      <div class="service__photo" role="img" aria-label="Photo of business professionals in an office" style="background:linear-gradient(135deg,#e9e4dc,#b9a48a 55%,#3c3c3c)"></div>
      <div class="service__caption"><em>Technology</em> Distribution</div>
      <p class="service__text">We supply hardware and software resources to clients in various business verticals. 7VLINK has sales partnership arrangements with key vendors...</p>
    </article>

    <div class="mission">
      <strong>7VLINK</strong> is committed to continuously building a customer-centric service delivery organization through the integration of strategic alliances, eople, processes and technologies, in order to continuously move up the value chain, while driving costs down, so as to maximize value delivered to our customers.
    </div>
  </section>

  <div class="partners" aria-label="Partner listings">
    <span class="partners__badge" style="width:145px"></span>
    <span class="partners__rule"></span>
    <span class="partners__badge" style="width:88px"></span>
    <span class="partners__rule"></span>
    <span class="partners__badge" style="width:95px"></span>
    <span class="partners__rule"></span>
    <span class="partners__badge" style="width:58px"></span>
  </div>

  <div class="band"></div>

  <footer class="footer">
    <div class="footer__col" style="left:60px">
      <div class="footer__title">SOLUTIONS</div>
      <span class="footer__link">Internet Services</span>
      <span class="footer__link">Residential Users</span>
      <span class="footer__link">Business</span>
    </div>
    <div class="footer__col" style="left:188px">
      <div class="footer__title">TECHNOLOGY PROJECTS</div>
      <span class="footer__link">Plorvex Advanced Services</span>
      <span class="footer__link">Networks and Infrastructure</span>
      <span class="footer__link">Software &amp; Enterprise Apps</span>
      <span class="footer__link">Systems Integration</span>
    </div>
    <div class="footer__col" style="left:375px">
      <div class="footer__title">MANAGED SERVICES</div>
      <span class="footer__link">Managed IT</span>
      <span class="footer__link">Sky Harbor</span>
      <span class="footer__link">Data Center &amp; Co-location</span>
      <span class="footer__link">Managed PBX</span>
      <span class="footer__link">Managed Video Conferencing</span>
    </div>
    <div class="footer__col" style="left:552px">
      <div class="footer__title">POSSIBILITIES</div>
      <span class="footer__link">7VLINK Labs</span>
      <span class="footer__link">Co-innovation</span>
    </div>

    <div class="footer__social" aria-label="Social links">
      <span></span><span></span><span></span><span></span>
    </div>

    <div class="footer__brand">
      <span class="brand__dot"></span>
      <span class="brand__name">7vlink</span>
    </div>
  </footer>

  <div class="copyright">© Copyright 2012, 7VLINK Nigeria Limited</div>
</body>
</html>
```